Wedding Startup Full Website Design

We've just completed our online platform and need to create a website that represents our brand and vision, and clearly communicates our features and value proposition to potential users. There are a minimum of 4 pages that need to be designed. One geared toward wedding professionals (venues/vendors/coordinators), another toward engaged couples, one showcasing features, and an 'About Us' page.

The designer will creative freedom to create a unique UI/UX as long as it represents our brand and is relevant to our target audience/market. The ideal candidate will be able to assume the mindset of someone working in the wedding industry and/or an engaged couple. Ability to create illustrations is a plus.

Copy will be provided as needed. We will reimburse for stock images (pending approval before purchasing), but sourcing the stock images will be the responsibility of the designer.

Our current website: https://www.trelmora.com
Updates

Our project has now been guaranteed! We look forward to finding the perfect design for our site pages!

Still waiting for a design that stands out from the rest and aligns with the creative brief.

Target Market(s)

Wedding Professionals and Engaged Couples

Industry/Entity Type

Wedding

Number of Pages Required

4 page

Font styles to use
Sans Serif

Colors
ffffff
fbd4d5
f59195
33a6d7
cadf82
86cfc6

Requirements
Must have
• Common sense stuff like having a unified brand that accurately represents our platform, speaks to our target market, and clearly articulates our vision
Nice to have
• Illustrations
Should not have
• Overly cheesy or childish. We want to be professional but still embrace the wedding culture.

```html
<!DOCTYPE html>
<html lang="en">
<head>
<meta charset="utf-8">
<title>Trelmora — Changing the Wedding Planning Process</title>
<link href="https://fonts.googleapis.com/css2?family=Oswald:wght@400;500;600&family=Open+Sans:wght@400;600;700&display=swap" rel="stylesheet">
<style>
:root{
  --white:#ffffff;
  --blush:#fbd4d5;
  --pink:#f59195;
  --pink-deep:#ee7e84;
  --blue:#33a6d7;
  --sky:#5bb8e6;
  --lime:#cadf82;
  --mint:#86cfc6;
  --sage:#6f9f97;
  --violet:#8c7fbf;
  --ink:#333438;
  --grey:#8a8c92;
  --line:#e5e6ea;
  --footer:#2e2f33;
}
*{box-sizing:border-box;margin:0;padding:0}
html,body{width:1200px;height:3604px;overflow:hidden}
body{font-family:"Open Sans",Arial,sans-serif;color:var(--ink);background:var(--white);position:relative}
a{text-decoration:none}
.heading{font-family:"Oswald","Arial Narrow",sans-serif;font-weight:500;text-transform:uppercase;letter-spacing:1px}
.section-title{font-family:"Oswald","Arial Narrow",sans-serif;font-weight:500;font-size:34px;line-height:1.2;text-align:center;text-transform:uppercase;letter-spacing:1px}
.section-title::after{content:"";display:block;width:60px;height:3px;background:var(--pink);margin:12px auto 0}
.btn{display:inline-block;font-family:"Oswald","Arial Narrow",sans-serif;font-size:15px;line-height:1.2;letter-spacing:2px;text-transform:uppercase;color:var(--white);background:var(--sky);padding:10px 40px;white-space:nowrap}
.brand{font-family:"Open Sans",Arial,sans-serif;font-weight:600;display:flex;align-items:center;gap:10px;white-space:nowrap}
.brand .dot{width:14px;height:14px;border-radius:50%;background:var(--blue)}

/* hero */
.hero{position:absolute;left:0;top:0;width:1200px;height:610px;background:linear-gradient(180deg,#ece7e2 0%,#d9dde0 40%,#cfd6cf 70%,#b9c2b4 100%)}
.hero .shade{position:absolute;inset:0;background:rgba(40,40,50,.18)}
.nav{position:absolute;left:0;top:0;width:1200px;height:70px;background:rgba(255,255,255,.88);display:flex;align-items:center;padding:0 60px}
.nav .brand{font-size:34px;color:var(--blue)}
.nav-links{display:flex;gap:18px;margin-left:200px;font-size:15px;white-space:nowrap}
.nav-links a{color:var(--ink);padding:6px 10px}
.nav-links a.active{background:var(--pink);color:var(--white)}
.nav-phone{margin-left:auto;font-size:15px;display:flex;align-items:center;gap:8px;white-space:nowrap}
.hero-title{position:absolute;top:250px;width:100%;text-align:center;color:var(--white);font-size:52px;line-height:1.1}
.hero-sub{position:absolute;top:322px;width:100%;text-align:center;color:var(--pink);font-family:"Oswald","Arial Narrow",sans-serif;font-size:22px;line-height:1.2;letter-spacing:4px;text-transform:uppercase}
.pillars{position:absolute;top:550px;left:80px;width:1040px;display:flex;gap:30px}
.pillar{flex:1;background:var(--white);height:110px;box-shadow:0 4px 14px rgba(0,0,0,.1);display:flex;gap:14px;padding:20px 22px;border-bottom:4px solid var(--pink)}
.pillar svg{flex:none}
.pillar h3{color:var(--pink);font-size:17px;font-weight:600;margin-bottom:4px}
.pillar p{font-size:13px;color:var(--grey);line-height:1.5}

/* get started */
.start{position:absolute;top:700px;left:0;width:1200px}
.steps{position:absolute;top:110px;left:160px;width:390px}
.step{display:flex;gap:22px;align-items:flex-start;margin-bottom:36px;padding:14px 0}
.step.current{background:var(--blush);margin-left:-30px;padding:14px 0 14px 30px}
.step .icon{width:66px;height:66px;border-radius:50%;background:var(--ink);flex:none;display:flex;align-items:center;justify-content:center}
.step.current .icon{background:var(--pink)}
.step h4{font-size:17px;font-weight:600;margin-bottom:4px}
.step.current h4{color:var(--pink)}
.step p{font-size:13px;color:var(--grey);line-height:1.55}
.screen-shot{position:absolute;top:110px;left:630px;width:420px;height:320px;border-radius:12px;background:linear-gradient(180deg,#eef0f4,#dfe2e8)}
.start .btn{position:absolute;top:482px;left:490px}

/* professionals */
.pros{position:absolute;top:1280px;left:0;width:1200px;height:580px;background:linear-gradient(135deg,#f3a3a7,var(--pink) 50%,#e98489)}
.pros .section-title{color:var(--white);padding-top:52px}
.pros .section-title::after{background:var(--white)}
.pro-cards{position:absolute;top:128px;left:80px;width:1040px;display:flex;gap:28px}
.pro-card{flex:1;background:var(--white);height:382px;position:relative}
.pro-card .photo{height:160px}
.pro-card h3{color:var(--pink);font-size:17px;font-weight:600;margin:18px 22px 8px}
.pro-card p{font-size:13px;color:var(--grey);line-height:1.55;margin:0 22px}
.pro-card .btn{position:absolute;left:0;bottom:0;width:100%;text-align:center;background:var(--sky)}
.pro-card .btn.dark{background:var(--ink)}

/* couples */
.couples{position:absolute;top:1900px;left:0;width:1200px}
.couple-grid{position:absolute;top:86px;left:80px;width:1040px;height:320px;display:flex}
.couple-tile{flex:1;color:var(--white);text-align:center;padding:36px 26px}
.couple-tile h3{font-size:17px;font-weight:600;margin:12px 0 10px}
.couple-tile p{font-size:13px;line-height:1.6;opacity:.95}
.t-sage{background:var(--sage)}.t-blue{background:var(--sky)}.t-violet{background:var(--violet)}.t-mint{background:#5fa8a0}

/* why choose */
.why{position:absolute;top:2312px;left:0;width:1200px;height:648px}
.why .photo{position:absolute;left:0;top:0;width:600px;height:648px;background:linear-gradient(160deg,#e9e2dc,#cfc3bb 45%,#a99a92 80%,#8c7e78)}
.why .label{position:absolute;left:0;bottom:60px;width:600px;height:70px;background:rgba(40,40,45,.7);color:var(--white);font-size:30px;display:flex;align-items:center;justify-content:center}
.why .panel{position:absolute;left:600px;top:0;width:600px;height:648px;background:var(--pink);padding:48px 60px}
.reason{display:flex;gap:20px;margin-bottom:20px}
.reason .ri{width:40px;height:40px;flex:none;border:2px solid var(--white);border-radius:6px}
.reason h4{color:var(--white);font-size:16px;font-weight:600;margin-bottom:3px}
.reason p{color:var(--blush);font-size:13px;line-height:1.5}
.why .btn{margin-left:60px;margin-top:8px}

/* contact */
.contact{position:absolute;top:2960px;left:0;width:1200px;height:528px;background:linear-gradient(180deg,#3a3537,#554b4b 50%,#2f2b2d)}
.contact .brand{position:absolute;top:60px;left:0;width:100%;justify-content:center;color:var(--white);font-size:34px}
.contact .intro{position:absolute;top:124px;width:100%;text-align:center;color:#d6d6d8;font-size:14px}
.field{position:absolute;border-bottom:1px solid rgba(255,255,255,.6);color:#d6d6d8;font-size:14px;padding-bottom:8px}
.contact .btn{position:absolute;top:400px;left:540px;padding:10px 44px}

/* footer */
.footer{position:absolute;top:3488px;left:0;width:1200px;height:116px;background:var(--footer);color:#c9cacf}
.footer .brand{position:absolute;left:80px;top:18px;font-size:30px;color:var(--white)}
.footer .copy{position:absolute;left:80px;top:78px;font-size:11px}
.footer h5{font-size:12px;color:var(--white);letter-spacing:1px;margin-bottom:4px;font-weight:600;line-height:1.3}
.quick{position:absolute;left:440px;top:12px;font-size:11px;line-height:1.5}
.social{position:absolute;left:700px;top:12px}
.social .circles{display:flex;gap:8px}
.social .circles span{width:24px;height:24px;border-radius:50%;background:var(--white)}
.footer .btn{position:absolute;right:80px;top:34px;font-size:13px;padding:9px 26px}
</style>
</head>
<body>

<section class="hero">
  <div role="img" aria-label="Photo of a bright wedding reception hall with tall windows and white floral arrangements" style="position:absolute;inset:0"></div>
  <div class="shade"></div>
  <nav class="nav">
    <div class="brand"><span class="dot"></span>Trelmora</div>
    <div class="nav-links">
      <a class="active" href="#">Home</a><a href="#">About Us</a><a href="#">Wedding Professionals</a><a href="#">Engaged Couples</a>
    </div>
    <div class="nav-phone">
      <svg width="14" height="14" viewBox="0 0 24 24"><path d="M6 2l4 4-2 3a12 12 0 006 6l3-2 4 4-3 3C9 20 4 15 3 5z" fill="var(--pink)"/></svg>
      (555) 014-2290
    </div>
  </nav>
  <h1 class="heading hero-title">Welcome to Trelmora</h1>
  <p class="hero-sub">We changing the wedding planning process!</p>
</section>

<div class="pillars">
  <div class="pillar">
    <svg width="40" height="40" viewBox="0 0 40 40"><circle cx="20" cy="20" r="17" fill="none" stroke="var(--pink)" stroke-width="2"/><path d="M20 29l-8-8a5 5 0 018-6 5 5 0 018 6z" fill="var(--pink)"/></svg>
    <div><h3>Inspire</h3><p>Inspire innovation and bridging dream weddings to life</p></div>
  </div>
  <div class="pillar">
    <svg width="40" height="40" viewBox="0 0 40 40"><rect x="6" y="8" width="28" height="26" rx="2" fill="none" stroke="var(--pink)" stroke-width="2"/><path d="M6 15h28M13 5v6M27 5v6" stroke="var(--pink)" stroke-width="2"/></svg>
    <div><h3>Plan</h3><p>For wedding professionals and couples to enjoy the wedding planning experience</p></div>
  </div>
  <div class="pillar">
    <svg width="40" height="40" viewBox="0 0 40 40"><path d="M6 32l9-10 6 5 13-15" fill="none" stroke="var(--pink)" stroke-width="2.5"/><path d="M28 12h6v6" fill="none" stroke="var(--pink)" stroke-width="2.5"/></svg>
    <div><h3>Grow</h3><p>Foster growth for our partners and within the wedding industry</p></div>
  </div>
</div>

<section class="start">
  <h2 class="section-title">How to Get Started</h2>
  <div class="steps">
    <div class="step current">
      <div class="icon"><svg width="28" height="28" viewBox="0 0 24 24"><rect x="5" y="3" width="14" height="18" rx="1" fill="none" stroke="#fff" stroke-width="2"/><path d="M8 8h8M8 12h8M8 16h5" stroke="#fff" stroke-width="2"/></svg></div>
      <div><h4>Sign Up</h4><p>Create a free account on Trelmora to access our collaborative tools</p></div>
    </div>
    <div class="step">
      <div class="icon"><svg width="30" height="30" viewBox="0 0 24 24"><circle cx="8" cy="8" r="3" fill="#fff"/><circle cx="16" cy="8" r="3" fill="#fff"/><path d="M2 19a6 6 0 0112 0zM10 19a6 6 0 0112 0z" fill="#fff"/></svg></div>
      <div><h4>Collaborate</h4><p>Work online with the application to deliver organized and manageable details</p></div>
    </div>
    <div class="step">
      <div class="icon"><svg width="28" height="28" viewBox="0 0 24 24"><circle cx="12" cy="12" r="3" fill="#fff"/><circle cx="4" cy="5" r="2" fill="#fff"/><circle cx="20" cy="5" r="2" fill="#fff"/><circle cx="12" cy="21" r="2" fill="#fff"/><path d="M4 5l8 7 8-7M12 12v9" stroke="#fff" stroke-width="1.5"/></svg></div>
      <div><h4>Connect</h4><p>Linking your board account within Trelmora to allow for seamless payments and monitoring</p></div>
    </div>
  </div>
  <div class="screen-shot" role="img" aria-label="Screenshot of the Trelmora planning dashboard shown on a laptop"></div>
  <a class="btn" href="#">Get Started</a>
</section>

<section class="pros">
  <h2 class="section-title">Wedding Professionals</h2>
  <div class="pro-cards">
    <article class="pro-card">
      <div class="photo" role="img" aria-label="Photo of an elegant reception venue set with round tables" style="background:linear-gradient(160deg,#f1e6dd,#d9c6b6 60%,#b9a392)"></div>
      <h3>Professional Venues</h3>
      <p>It is a long established fact that a reader will be distracted by the readable content of a page when looking at its layout.</p>
      <a class="btn" href="#">Search Venues</a>
    </article>
    <article class="pro-card">
      <div class="photo" role="img" aria-label="Photo of a wedding vendor meeting with a client" style="background:linear-gradient(160deg,#eef0f2,#cfd4da 55%,#a9b1ba)"></div>
      <h3>Professional Vendors</h3>
      <p>It is a long established fact that a reader will be distracted by the readable content of a page when looking at its layout.</p>
      <a class="btn dark" href="#">Search Vendors</a>
    </article>
    <article class="pro-card">
      <div class="photo" role="img" aria-label="Photo of a coordinator arranging table settings" style="background:linear-gradient(160deg,#f4f2f0,#d8d3cf 55%,#7c7472)"></div>
      <h3>Coordinators</h3>
      <p>It is a long established fact that a reader will be distracted by the readable content of a page when looking at its layout.</p>
      <a class="btn" href="#">Search Coordinators</a>
    </article>
  </div>
</section>

<section class="couples">
  <h2 class="section-title">Engaged Couples</h2>
  <div class="couple-grid">
    <div class="couple-tile t-sage">
      <svg width="40" height="28" viewBox="0 0 40 28"><path d="M2 14C8 4 32 4 38 14 32 24 8 24 2 14z" fill="none" stroke="#fff" stroke-width="2.5"/><circle cx="20" cy="14" r="5" fill="#fff"/></svg>
      <h3>Vision</h3><p>Every couple has a dream of what their special day will be like; share your vision and inspiration boards with your planning team.</p>
    </div>
    <div class="couple-tile t-blue">
      <svg width="32" height="32" viewBox="0 0 32 32"><path d="M4 28l4-12L24 2l6 6-16 16z" fill="none" stroke="#fff" stroke-width="2.5"/></svg>
      <h3>Create</h3><p>Taking your ideas and turning them into plans is simple with our tools; build checklists, budgets and guest lists together.</p>
    </div>
    <div class="couple-tile t-violet">
      <svg width="34" height="32" viewBox="0 0 34 32"><rect x="2" y="4" width="30" height="26" fill="none" stroke="#fff" stroke-width="2.5"/><path d="M2 12h30M10 2v6M24 2v6" stroke="#fff" stroke-width="2.5"/></svg>
      <h3>Organize</h3><p>Keep every detail in one place so nothing is forgotten; track vendors, contracts and timelines from a single board.</p>
    </div>
    <div class="couple-tile t-mint">
      <svg width="34" height="32" viewBox="0 0 34 32"><path d="M2 30V4M2 30h30" stroke="#fff" stroke-width="2.5"/><path d="M8 22l7-8 6 5 9-11" fill="none" stroke="#fff" stroke-width="2.5"/></svg>
      <h3>Monitor</h3><p>It's important to stay in the know; follow progress, payments and messages so your planning stays calm and on track.</p>
    </div>
  </div>
</section>

<section class="why">
  <div class="photo" role="img" aria-label="Photo of a bride and groom embracing under falling petals"></div>
  <div class="label heading">Why Choose Trelmora</div>
  <div class="panel">
    <div class="reason"><span class="ri"></span><div><h4>Saves Everyone Time</h4><p>Shared planning boards remove endless emails and calls, letting everyone focus on what matters.</p></div></div>
    <div class="reason"><span class="ri"></span><div><h4>Simplified Organization</h4><p>Checklists, budgets and timelines live together, so every detail is easy to find and update.</p></div></div>
    <div class="reason"><span class="ri"></span><div><h4>Better Client Reviews</h4><p>Happy couples share their experience, helping professionals grow trust and win new bookings.</p></div></div>
    <div class="reason"><span class="ri"></span><div><h4>Easier Collaboration</h4><p>Couples, venues, vendors and coordinators work as one team with clear roles and updates.</p></div></div>
    <div class="reason"><span class="ri"></span><div><h4>Accessible on Any Device</h4><p>Plan from anywhere on a phone, tablet or laptop, with changes synced instantly for all.</p></div></div>
    <a class="btn" href="#">Get Started</a>
  </div>
</section>

<section class="contact">
  <div role="img" aria-label="Photo of a couple holding hands with wedding rings, darkened" style="position:absolute;inset:0"></div>
  <div class="brand"><span class="dot"></span>Trelmora</div>
  <p class="intro">Fill the form to contact us for any query</p>
  <div class="field" style="top:196px;left:190px;width:390px">Name</div>
  <div class="field" style="top:196px;left:620px;width:390px">Email</div>
  <div class="field" style="top:264px;left:190px;width:820px;height:90px">Message</div>
  <a class="btn" href="#">Send</a>
</section>

<footer class="footer">
  <div class="brand"><span class="dot"></span>Trelmora</div>
  <p class="copy">Copyright © 2018 | All rights reserved</p>
  <div class="quick"><h5>QUICK LINKS</h5>Home<br>About Us<br>Wedding Professionals<br>Engaged Couples</div>
  <div class="social"><h5>SOCIAL LINKS</h5><div class="circles"><span></span><span></span><span></span></div></div>
  <a class="btn" href="#">Access Demo</a>
</footer>

</body>
</html>
```